Packing for Razor Blade VORELIN

Dears: We need a packing design. The product is an Disposable Razor Blade. We are a company in Brazil.

The packing consists in a bag package which the Disposables Razos are placed. 5 units into each bag.

The bag is not 100% printed and should let a space to the customer see the razors inside. Some competitors uses oval circle. I attached competitor package (Tove Marigold)

The background color should be blue, this color tonality should vary its magnitude from dark blue to soft blue. Blue is a good color for personal care products because customer can take the impression of cleanness, especially for razor blade which has the fuction to shave.

You can feel free to add other colors however it can not be much colorfull because it may get trouble to printer company print it. Silver is good.

You can feel free to do details. You can feel free also to place the logo above the package or at bottom of it.

Dimmensions:
Heigh 24cm
Width 10cm

Featuring
- Featuring: Handle with Grip. In Portuguese - (Cabo Aderente)
- Featuring: 2 Razors. In portuguese - (Duas Lâminas)

Reason: I stayed many days with out providing feedbacks. I want to give more time for you .

Target Market(s)

Mans ( for woman we will design other package )

Requirements
Nice to have
• maybe some tears as a wet surface...
pls can feel free

```html
<!DOCTYPE html>
<html lang="en">
<head>
<meta charset="utf-8">
<title>VORELIN Disposable Razors – Packaging</title>
<link href="https://fonts.googleapis.com/css2?family=Arimo:wght@400;700&display=swap" rel="stylesheet">
<style>
  :root {
    --stage: #5d5d61;
    --navy: #020a2e;
    --blue-pale: #8fd3f4;
    --blue-soft: #5cb8e8;
    --blue-mid: #3a9ad8;
    --blue-deep: #1a6fbe;
    --charcoal: #25272b;
    --charcoal-deep: #1b1d20;
    --white: #ffffff;
    --note: #e6e6e6;
    --hole: #7b7d81;
  }
  * { margin: 0; padding: 0; box-sizing: border-box; }
  html, body { width: 1200px; height: 900px; overflow: hidden; }
  body {
    background: var(--stage);
    font-family: "Arimo", Arial, sans-serif;
    position: relative;
  }
  .package { position: absolute; width: 284px; height: 682px; }
  .package--dark-window { left: 225px; top: 108px; }
  .package--light-window { left: 731px; top: 106px; }
  .package svg { display: block; width: 284px; height: 682px; }

  .brand-name {
    font-weight: 700;
    font-size: 31px;
    letter-spacing: 1.5px;
    fill: var(--white);
  }
  .product-title {
    font-weight: 700;
    font-size: 22px;
    fill: var(--white);
    stroke: var(--blue-deep);
    stroke-width: 4px;
    paint-order: stroke;
  }
  .feature-title { font-weight: 700; font-size: 15px; fill: var(--white); }
  .feature-title--small { font-size: 13px; }
  .feature-digit { font-size: 20px; }
  .feature-sub { font-weight: 700; font-size: 11px; fill: var(--white); }
  .unit-count {
    font-weight: 700;
    font-size: 52px;
    fill: var(--white);
    stroke: var(--blue-deep);
    stroke-width: 6px;
    paint-order: stroke;
  }

  .annotation {
    position: absolute;
    left: 510px;
    top: 312px;
    width: 145px;
    color: var(--note);
  }
  .annotation__label { font-size: 18px; text-align: right; padding-right: 2px; line-height: 28px; }
  .annotation__rule { height: 1px; background: var(--note); }
  .annotation__detail { font-size: 12px; text-align: right; line-height: 16px; padding: 6px 2px 8px 0; }
</style>
</head>
<body>

<svg width="0" height="0" style="position:absolute" aria-hidden="true">
  <defs>
    <linearGradient id="body-blue" x1="0" y1="0" x2="1" y2="1">
      <stop offset="0" stop-color="#8fd3f4"/>
      <stop offset="0.45" stop-color="#4aa8df"/>
      <stop offset="1" stop-color="#1a6fbe"/>
    </linearGradient>
    <linearGradient id="base-blue" x1="0" y1="0" x2="1" y2="1">
      <stop offset="0" stop-color="#5cb8e8"/>
      <stop offset="1" stop-color="#1766b5"/>
    </linearGradient>
    <linearGradient id="band-blue" x1="0" y1="0" x2="1" y2="1">
      <stop offset="0" stop-color="#6cc4ef"/>
      <stop offset="1" stop-color="#2d8fd2"/>
    </linearGradient>
    <linearGradient id="silver-rim" x1="0" y1="0" x2="1" y2="1">
      <stop offset="0" stop-color="#f4f4f4"/>
      <stop offset="0.5" stop-color="#8b8d91"/>
      <stop offset="1" stop-color="#d8d8da"/>
    </linearGradient>
    <linearGradient id="feature-box" x1="0" y1="0" x2="0" y2="1">
      <stop offset="0" stop-color="#3d6b93"/>
      <stop offset="0.5" stop-color="#1c2532"/>
      <stop offset="1" stop-color="#3f74a2"/>
    </linearGradient>
    <linearGradient id="charcoal-fill" x1="0" y1="0" x2="0" y2="1">
      <stop offset="0" stop-color="#2e3034"/>
      <stop offset="1" stop-color="#1b1d20"/>
    </linearGradient>
    <linearGradient id="window-dark" x1="0" y1="0" x2="1" y2="1">
      <stop offset="0" stop-color="#4a4c50"/>
      <stop offset="0.6" stop-color="#2c2e32"/>
      <stop offset="1" stop-color="#1f2124"/>
    </linearGradient>
    <linearGradient id="window-light" x1="0" y1="0" x2="1" y2="1">
      <stop offset="0" stop-color="#fafafa"/>
      <stop offset="0.6" stop-color="#eeeeef"/>
      <stop offset="1" stop-color="#d9dadc"/>
    </linearGradient>
    <linearGradient id="swoosh-white" x1="0" y1="0" x2="1" y2="0">
      <stop offset="0" stop-color="#bfc0c3"/>
      <stop offset="0.6" stop-color="#f2f2f3"/>
      <stop offset="1" stop-color="#d2d3d5"/>
    </linearGradient>
  </defs>
</svg>

<!-- Variant A: dark backing behind window -->
<div class="package package--dark-window">
  <svg viewBox="0 0 284 682">
    <rect class="body-panel" width="284" height="682" fill="url(#body-blue)"/>
    <path class="light-swoosh" d="M12 150 C60 140 110 160 130 215 C110 225 70 180 12 150 Z" fill="#eaf6fd" opacity="0.85"/>
    <path class="charcoal-sweep" d="M130 140 H284 V682 H0 V400 C40 340 120 300 130 140 Z" fill="url(#charcoal-fill)"/>
    <path class="lower-band" d="M0 560 C80 560 160 530 230 470 L230 500 C160 570 80 600 0 610 Z" fill="#3c3e42"/>
    <path class="base-blue" d="M70 682 C160 650 230 570 284 480 V682 Z" fill="url(#base-blue)"/>
    <path class="window-rim" d="M284 112 C140 200 95 440 178 682 L204 682 C230 600 255 520 284 450 Z" fill="url(#silver-rim)"/>
    <path class="window razor-image" role="img" aria-label="Transparent window showing a disposable two-blade razor"
          d="M284 128 C156 212 112 440 192 670 C222 590 252 510 284 440 Z" fill="url(#window-dark)"/>

    <rect class="header" width="284" height="140" fill="var(--navy)"/>
    <circle class="hang-hole" cx="145" cy="20" r="7" fill="var(--hole)"/>
    <text class="brand-name" x="142" y="78" text-anchor="middle">VORELIN</text>
    <text class="product-title" x="142" y="120" text-anchor="middle">Disposable Razors</text>

    <rect x="12" y="304" width="116" height="83" fill="url(#feature-box)" stroke="#4f8fcf" stroke-width="3"/>
    <text class="feature-title" x="28" y="345"><tspan class="feature-digit">2</tspan> Razors</text>
    <text class="feature-sub" x="28" y="359">Duas Lâminas</text>

    <rect x="12" y="405" width="146" height="82" fill="url(#feature-box)" stroke="#4f8fcf" stroke-width="3"/>
    <text class="feature-title feature-title--small" x="26" y="444">Handle with Grip</text>
    <text class="feature-sub" x="26" y="462">Cabo Aderente</text>

    <text class="unit-count" x="235" y="648" text-anchor="middle">5</text>
  </svg>
</div>

<div class="annotation">
  <p class="annotation__label">Transparent</p>
  <div class="annotation__rule"></div>
  <p class="annotation__detail">Changable image<br>for 5 items</p>
  <div class="annotation__rule"></div>
</div>

<!-- Variant B: light backing behind window -->
<div class="package package--light-window">
  <svg viewBox="0 0 284 682">
    <rect class="body-panel" width="284" height="682" fill="url(#charcoal-fill)"/>
    <path class="blue-band" d="M0 222 C70 200 150 205 200 225 V392 C130 372 60 378 0 392 Z" fill="url(#band-blue)"/>
    <path class="band-highlight" d="M40 246 C70 236 110 236 130 240 L128 258 C100 254 70 255 42 262 Z" fill="#e8f5fc" opacity="0.85"/>
    <path class="white-swoosh" d="M0 400 C60 372 140 374 200 398 V432 C130 416 60 418 0 432 Z" fill="url(#swoosh-white)"/>
    <path class="base-blue" d="M70 682 C160 650 230 570 284 480 V682 Z" fill="url(#base-blue)"/>
    <path class="window-rim" d="M284 112 C140 200 95 440 178 682 L204 682 C230 600 255 520 284 450 Z" fill="url(#silver-rim)"/>
    <path class="window razor-image" role="img" aria-label="Transparent window showing a disposable two-blade razor"
          d="M284 128 C156 212 112 440 192 670 C222 590 252 510 284 440 Z" fill="url(#window-light)"/>

    <rect class="header" width="284" height="144" fill="var(--navy)"/>
    <circle class="hang-hole" cx="141" cy="22" r="7" fill="var(--hole)"/>
    <text class="brand-name" x="142" y="80" text-anchor="middle">VORELIN</text>
    <text class="product-title" x="142" y="124" text-anchor="middle">Disposable Razors</text>

    <rect x="10" y="284" width="117" height="83" fill="url(#feature-box)" stroke="#4f8fcf" stroke-width="3"/>
    <text class="feature-title" x="28" y="325"><tspan class="feature-digit">2</tspan> Razors</text>
    <text class="feature-sub" x="28" y="339">Duas Lâminas</text>

    <rect x="11" y="451" width="165" height="82" fill="url(#feature-box)" stroke="#4f8fcf" stroke-width="3"/>
    <text class="feature-title" x="26" y="491">Handle with Grip</text>
    <text class="feature-sub" x="26" y="506">Cabo Aderente</text>

    <text class="unit-count" x="242" y="658" text-anchor="middle">5</text>
  </svg>
</div>

</body>
</html>
```